Current Product Line needs to expand with additional products

We have a current established product but will need to add a line extension. We are open to change however we do need to keep the "Verdanox by Pellarino" Name as the brand it would be good if we can keep the same kind of look with different colors however we do need the name of the different lines. Ex: Verda nox Mega-Strength Multi-Vitamin, Verdanox by Pellarino Turmeric, Verdanox by Pellarino, Vitamin C etc. Looking for different colors for each line extension. Once we have the labels we will need additional work for other projects. Our website is verdanox-example.com. Attached is our current label as well as our new logo and a version of the line extension. Thank you

```html
<!DOCTYPE html>
<html lang="en">
<head>
<meta charset="utf-8">
<title>Verdanox by Pellarino – Label Line Extension</title>
<link href="https://fonts.googleapis.com/css2?family=Archivo+Black&family=Arimo:wght@400;700&family=Great+Vibes&family=Oswald:wght@600&family=Titillium+Web:wght@400;700&display=swap" rel="stylesheet">
<style>
  :root{
    --canvas:#8f8f8f;
    --paper:#ffffff;
    --ink:#111111;
    --rule:#222222;
    --body-font:"Arimo", Arial, sans-serif;
  }
  .multi{ --band:#e4661e; --logo:#17982a; --grade:#0c7f30; --grade-dark:#075c22; --accent:#22b934; --pill:#1fbf2e; --frame:#e879d6; --softgel-text:#2f8a2a; }
  .turmeric{ --band:#2fd8c4; --logo:#b0144f; --grade:#5f0022; --grade-dark:#44001a; --accent:#d3134c; --pill:#e41b53; --frame:#7fe6c9; --softgel-text:#234a9e; }
  .vitc{ --band:#d4401c; --logo:#b35a26; --grade:#4d3b0f; --grade-dark:#3a2c08; --accent:#f08a18; --pill:#e2481a; --frame:#e879d6; --softgel-text:#6b5a1a; }

  *{box-sizing:border-box;margin:0;padding:0}
  html,body{width:960px;height:1200px;overflow:hidden}
  body{background:var(--canvas);position:relative;font-family:var(--body-font);color:var(--ink)}

  .label{position:absolute;left:50px;width:860px;height:327px;background:var(--paper);box-shadow:3px 4px 8px rgba(0,0,0,.35);overflow:hidden}
  .label--one{top:56px}
  .label--two{top:436px}
  .label--three{top:820px}

  .label__band{position:absolute;left:6px;right:6px;top:6px;height:34px;background:var(--band);border-radius:10px 10px 0 0}
  .label__frame{position:absolute;left:6px;right:6px;top:6px;bottom:6px;border:1px solid var(--frame);border-radius:10px;pointer-events:none}

  .potency{position:absolute;left:42px;top:13px;font:700 12px "Titillium Web",sans-serif;color:#fff}
  .professional{position:absolute;left:350px;width:180px;text-align:center;top:8px;font:700 19px "Titillium Web",sans-serif;color:#fff;letter-spacing:.3px}
  .directions{position:absolute;left:637px;top:15px;font:700 6.4px var(--body-font);color:#fff}

  .seal{position:absolute;left:268px;top:10px;width:56px;height:48px}

  .story{position:absolute;left:24px;top:56px;width:216px;font:700 7.5px/8.5px var(--body-font);text-align:justify;color:#111}
  .story p{margin-bottom:7px}

  .disclaimer{position:absolute;left:18px;top:286px;width:226px;height:26px;border:1.2px solid #111;font:700 5.6px/8px "Arimo",sans-serif;text-align:center;padding-top:3px}

  .brand{position:absolute;left:350px;width:180px;text-align:center;top:46px;font:400 42px/38px "Archivo Black",sans-serif;color:var(--logo);letter-spacing:-1px}
  .brand sup{position:absolute;right:6px;top:-2px;font:400 6px var(--body-font);color:#888;letter-spacing:0}
  .line-name{position:absolute;left:280px;width:310px;text-align:center;top:128px;font:400 19px "Great Vibes",cursive;color:var(--grade)}

  .grade{position:absolute;left:272px;top:163px;width:318px;height:31px;background:linear-gradient(180deg,var(--grade),var(--grade-dark));color:#fff;text-align:center;font:600 16px/31px "Oswald",sans-serif;letter-spacing:.4px}

  .features{position:absolute;left:336px;top:206px;list-style:none;font:400 12.5px/14.6px "Titillium Web",sans-serif;color:#111}
  .features li::before{content:"✓";color:var(--accent);font-weight:700;margin-right:4px}

  .pill{position:absolute;left:500px;width:70px;height:16px;border-radius:8px;background:var(--pill);color:#fff;font:400 10px/16px "Titillium Web",sans-serif;padding-left:21px;box-shadow:0 1px 2px rgba(0,0,0,.25)}
  .pill small{font-size:7px}
  .pill__drop{position:absolute;left:-4px;top:-6px;width:22px;height:25px}
  .pill__drop span{position:absolute;left:0;right:0;top:9px;text-align:center;font:400 7px "Titillium Web",sans-serif;color:#333}
  .pill--epa{top:215px}
  .pill--dha{top:249px}

  .total{position:absolute;left:490px;top:283px;width:92px;height:30px;border-radius:15px;background:var(--pill);color:#fff;text-align:center;font:700 italic 13px/13px "Titillium Web",sans-serif;padding-top:2px;box-shadow:0 2px 4px rgba(0,0,0,.3)}
  .total small{font-size:9px}
  .total em{display:block;font-size:9.5px;line-height:12px}

  .citrus{position:absolute;left:273px;top:258px;width:28px;height:28px;border-radius:50%;background:radial-gradient(circle at 40% 40%,#ffd34a,#f38a1e 60%,#7cc242)}
  .citrus-note{position:absolute;left:252px;top:292px;width:72px;text-align:center;font:700 italic 8px/10px var(--body-font)}
  .softgels{position:absolute;left:328px;top:303px;font:400 8.4px "Titillium Web",sans-serif;color:var(--softgel-text)}

  .facts{position:absolute;left:634px;top:32px;width:186px;height:182px;border:1.6px solid var(--rule);padding:3px 8px 0 8px}
  .facts h2{font:400 15.5px/17px "Archivo Black",sans-serif;letter-spacing:.4px}
  .facts__serving{display:flex;justify-content:space-between;font:400 5.8px var(--body-font);border-bottom:4px solid var(--rule);padding-bottom:3px}
  .facts__row{display:flex;justify-content:space-between;font:400 7px/11.4px var(--body-font);border-bottom:.6px solid #555}
  .facts__row--head{border-bottom:2px solid var(--rule)}
  .facts__row--split{border-top:1.4px solid var(--rule)}
  .facts__row--sub{padding-left:6px}
  .facts__row--other{padding-left:3px}
  .facts__row--total{border-bottom:2px solid var(--rule);font-weight:700}
  .facts__row span:first-child small{font-size:5.8px;font-weight:400}
  .facts__foot{font:400 5.6px/7px var(--body-font);padding-top:3px;padding-left:2px}

  .ingredients{position:absolute;left:634px;top:217px;width:196px;font:700 6.3px/7.6px var(--body-font)}
  .warning{position:absolute;left:634px;top:246px;width:200px;font:400 5.9px/7.4px var(--body-font)}
  .warning b{font-weight:700}
  .origin{position:absolute;left:634px;top:267px;width:200px;font:400 5.2px/6.4px var(--body-font);padding-left:25px}
  .origin svg{position:absolute;left:0;top:1px}
  .contact{position:absolute;left:659px;top:282px;font:700 9px var(--body-font)}
  .storage{position:absolute;left:634px;top:296px;width:200px;font:700 6.2px/7.4px var(--body-font)}
</style>
</head>
<body>

<!-- Multi-Vitamin line -->
<section class="label label--one multi">
  <div class="label__band"></div>
  <div class="label__frame"></div>
  <div class="potency">High Potency Triglyceride Form</div>
  <svg class="seal" viewBox="0 0 56 48" aria-hidden="true"><circle cx="28" cy="24" r="22" fill="#1d8f2b"/><rect x="2" y="19" width="52" height="10" fill="#2fb341"/></svg>
  <div class="professional">PROFESSIONAL</div>
  <div class="directions">Directions: Take one or two softgels daily.</div>

  <div class="story">
    <p>Each fish gelatin capsule of Verda nox™ contains 1350 mg of Ultra-Intensity-Omega-3 (UIO-3) fish oil, which is our unique blend of EPA and DHA (55:25) in the triglyceride form. One capsule meets the recommendation of the National Cardio Council. Two capsules provide over 2700 mg of UIO-3 and 2500 mg of total omega-3: making Verda nox™ one of the highest professional grade fish oils available.</p>
    <p>Our specially formulated capsule was developed by Dr. Pellarino, an award-winning pioneer in the pharmaceutical industry. In research performed over decades, purified omega-3 is reported to promote healthy cholesterol and triglyceride levels, as well as supporting our heart, brain, and eyes.</p>
    <p>More recently, scientific research reports that the essential fatty acids as in Verda nox™ can help joint function and the health of the immune system. Especially because of our ultra-intensity triglyceride form, absorption of Verda nox™ is superior to other fish oil products with less fishy taste or burping.</p>
  </div>
  <div class="disclaimer">*These statements have not been evaluated by the Food and Drug Administration.<br>This product is not intended to diagnose, treat, cure or prevent disease.</div>

  <div class="brand">Verda<br>nox<sup>TM</sup></div>
  <div class="line-name">Mega-Strength Multi-Vitamin</div>
  <div class="grade">PHARMACEUTICAL GRADE</div>
  <ul class="features">
    <li>Triglyceride Form</li><li>Fish Gelatin</li><li>Clinically Proven Ratio</li><li>Superior Absorption</li><li>Ultra-Intensity Omega-3</li>
  </ul>
  <div class="pill pill--epa"><div class="pill__drop"><svg width="22" height="25" viewBox="0 0 22 25"><path d="M11 1 C15 8 20 12 20 16 A9 9 0 0 1 2 16 C2 12 7 8 11 1Z" fill="#f6b41c"/></svg><span>EPA</span></div>1500 <small>mg</small></div>
  <div class="pill pill--dha"><div class="pill__drop"><svg width="22" height="25" viewBox="0 0 22 25"><path d="M11 1 C15 8 20 12 20 16 A9 9 0 0 1 2 16 C2 12 7 8 11 1Z" fill="#f6b41c"/></svg><span>DHA</span></div>680 <small>mg</small></div>
  <div class="total">2500<small>mg</small><em>Total Omega-3</em></div>
  <div class="citrus" role="img" aria-label="Orange and lemon slices illustration"></div>
  <div class="citrus-note">Fresh Citrus Taste<br>Burp-Free</div>
  <div class="softgels">90 SOFTGELS DIETARY SUPPLEMENT</div>

  <div class="facts">
    <h2>Supplement Facts</h2>
    <div class="facts__serving"><span>Serving Size: 2 Softgels</span><span>Servings Per Container: 45</span></div>
    <div class="facts__row facts__row--head"><span>Amount Per Softgel Serving</span><span>% Daily Value*</span></div>
    <div class="facts__row"><span>Calories</span><span>30&nbsp;&nbsp;&nbsp;&nbsp;&nbsp;&nbsp;&nbsp;</span></div>
    <div class="facts__row"><span>Total Fat</span><span>3 g&nbsp;&nbsp;&nbsp;4%</span></div>
    <div class="facts__row"><span>Saturated Fat</span><span>0 g&nbsp;&nbsp;&nbsp;0%</span></div>
    <div class="facts__row"><span>Trans Fat</span><span>0 g&nbsp;&nbsp;1†&nbsp;</span></div>
    <div class="facts__row facts__row--split"><span><b>UIO-3</b> <small>(Fish Oil Concentrate)</small></span><span>2,750mg&nbsp;&nbsp;†&nbsp;&nbsp;</span></div>
    <div class="facts__row facts__row--sub"><span><b>EPA</b> <small>(Eicosapentaenoic Acid)</small></span><span>1,500mg&nbsp;&nbsp;†&nbsp;&nbsp;</span></div>
    <div class="facts__row facts__row--sub"><span><b>DHA</b> <small>(Docosahexaenoic Acid)</small></span><span>680mg&nbsp;&nbsp;†&nbsp;&nbsp;</span></div>
    <div class="facts__row facts__row--other"><span>Other Omega-3s</span><span>320mg&nbsp;&nbsp;†&nbsp;&nbsp;</span></div>
    <div class="facts__row facts__row--total"><span>Total Omega-3 Triglyceride</span><span>2,500mg&nbsp;&nbsp;†&nbsp;&nbsp;</span></div>
    <div class="facts__foot">* Daily Value based on a 2000 Calorie diet<br>† Daily Value not established</div>
  </div>
  <div class="ingredients">Other Ingredients: Gelatin capsule (fish gelatin, glycerin, purified water and natural flavor), d-limonene, Vitamin E and mixed tocopherols.</div>
  <div class="warning"><b>Warning:</b> Contains purified fish oil (from anchovies and sardines) gelatin (tilapia &amp; carp)</div>
  <div class="origin"><svg width="21" height="12" viewBox="0 0 21 12" aria-hidden="true"><rect width="21" height="12" fill="#c8102e"/><rect y="2" width="21" height="1.7" fill="#fff"/><rect y="5.4" width="21" height="1.7" fill="#fff"/><rect y="8.8" width="21" height="1.7" fill="#fff"/><rect width="9" height="6.5" fill="#3c3b6e"/></svg>Manufactured in USA with ingredients from around the world<br>42 Harbor Point Rd. Suite 12 , Palm Cove, FL 00000</div>
  <div class="contact">555.010.2427 | verdanox-example.com</div>
  <div class="storage">Store in a cool dry place. Do not take if tamper-evident seal is broken or missing. Keep out of reach of children</div>
</section>

<!-- Turmeric line -->
<section class="label label--two turmeric">
  <div class="label__band"></div>
  <div class="label__frame"></div>
  <div class="potency">High Potency Triglyceride Form</div>
  <svg class="seal" viewBox="0 0 56 48" aria-hidden="true"><circle cx="28" cy="24" r="22" fill="#b3123f"/><rect x="2" y="19" width="52" height="10" fill="#2fb341"/></svg>
  <div class="professional">PROFESSIONAL</div>
  <div class="directions">Directions: Take one or two softgels daily.</div>

  <div class="story">
    <p>Each fish gelatin capsule of Verda nox™ contains 1350 mg of Ultra-Intensity-Omega-3 (UIO-3) fish oil, which is our unique blend of EPA and DHA (55:25) in the triglyceride form. One capsule meets the recommendation of the National Cardio Council. Two capsules provide over 2700 mg of UIO-3 and 2500 mg of total omega-3: making Verda nox™ one of the highest professional grade fish oils available.</p>
    <p>Our specially formulated capsule was developed by Dr. Pellarino, an award-winning pioneer in the pharmaceutical industry. In research performed over decades, purified omega-3 is reported to promote healthy cholesterol and triglyceride levels, as well as supporting our heart, brain, and eyes.</p>
    <p>More recently, scientific research reports that the essential fatty acids as in Verda nox™ can help joint function and the health of the immune system. Especially because of our ultra-intensity triglyceride form, absorption of Verda nox™ is superior to other fish oil products with less fishy taste or burping.</p>
  </div>
  <div class="disclaimer">*These statements have not been evaluated by the Food and Drug Administration.<br>This product is not intended to diagnose, treat, cure or prevent disease.</div>

  <div class="brand">Verda<br>nox<sup>TM</sup></div>
  <div class="line-name">by Pellarino Turmeric</div>
  <div class="grade">PHARMACEUTICAL GRADE</div>
  <ul class="features">
    <li>Triglyceride Form</li><li>Fish Gelatin</li><li>Clinically Proven Ratio</li><li>Superior Absorption</li><li>Ultra-Intensity Omega-3</li>
  </ul>
  <div class="pill pill--epa"><div class="pill__drop"><svg width="22" height="25" viewBox="0 0 22 25"><path d="M11 1 C15 8 20 12 20 16 A9 9 0 0 1 2 16 C2 12 7 8 11 1Z" fill="#b8e02a"/></svg><span>EPA</span></div>1500 <small>mg</small></div>
  <div class="pill pill--dha"><div class="pill__drop"><svg width="22" height="25" viewBox="0 0 22 25"><path d="M11 1 C15 8 20 12 20 16 A9 9 0 0 1 2 16 C2 12 7 8 11 1Z" fill="#b8e02a"/></svg><span>DHA</span></div>680 <small>mg</small></div>
  <div class="total">2500<small>mg</small><em>Total Omega-3</em></div>
  <div class="citrus" role="img" aria-label="Orange and lemon slices illustration"></div>
  <div class="citrus-note">Fresh Citrus Taste<br>Burp-Free</div>
  <div class="softgels">90 SOFTGELS DIETARY SUPPLEMENT</div>

  <div class="facts">
    <h2>Supplement Facts</h2>
    <div class="facts__serving"><span>Serving Size: 2 Softgels</span><span>Servings Per Container: 45</span></div>
    <div class="facts__row facts__row--head"><span>Amount Per Softgel Serving</span><span>% Daily Value*</span></div>
    <div class="facts__row"><span>Calories</span><span>30&nbsp;&nbsp;&nbsp;&nbsp;&nbsp;&nbsp;&nbsp;</span></div>
    <div class="facts__row"><span>Total Fat</span><span>3 g&nbsp;&nbsp;&nbsp;4%</span></div>
    <div class="facts__row"><span>Saturated Fat</span><span>0 g&nbsp;&nbsp;&nbsp;0%</span></div>
    <div class="facts__row"><span>Trans Fat</span><span>0 g&nbsp;&nbsp;1†&nbsp;</span></div>
    <div class="facts__row facts__row--split"><span><b>UIO-3</b> <small>(Fish Oil Concentrate)</small></span><span>2,750mg&nbsp;&nbsp;†&nbsp;&nbsp;</span></div>
    <div class="facts__row facts__row--sub"><span><b>EPA</b> <small>(Eicosapentaenoic Acid)</small></span><span>1,500mg&nbsp;&nbsp;†&nbsp;&nbsp;</span></div>
    <div class="facts__row facts__row--sub"><span><b>DHA</b> <small>(Docosahexaenoic Acid)</small></span><span>680mg&nbsp;&nbsp;†&nbsp;&nbsp;</span></div>
    <div class="facts__row facts__row--other"><span>Other Omega-3s</span><span>320mg&nbsp;&nbsp;†&nbsp;&nbsp;</span></div>
    <div class="facts__row facts__row--total"><span>Total Omega-3 Triglyceride</span><span>2,500mg&nbsp;&nbsp;†&nbsp;&nbsp;</span></div>
    <div class="facts__foot">* Daily Value based on a 2000 Calorie diet<br>† Daily Value not established</div>
  </div>
  <div class="ingredients">Other Ingredients: Gelatin capsule (fish gelatin, glycerin, purified water and natural flavor), d-limonene, Vitamin E and mixed tocopherols.</div>
  <div class="warning"><b>Warning:</b> Contains purified fish oil (from anchovies and sardines) gelatin (tilapia &amp; carp)</div>
  <div class="origin"><svg width="21" height="12" viewBox="0 0 21 12" aria-hidden="true"><rect width="21" height="12" fill="#c8102e"/><rect y="2" width="21" height="1.7" fill="#fff"/><rect y="5.4" width="21" height="1.7" fill="#fff"/><rect y="8.8" width="21" height="1.7" fill="#fff"/><rect width="9" height="6.5" fill="#3c3b6e"/></svg>Manufactured in USA with ingredients from around the world<br>42 Harbor Point Rd. Suite 12 , Palm Cove, FL 00000</div>
  <div class="contact">555.010.2427 | verdanox-example.com</div>
  <div class="storage">Store in a cool dry place. Do not take if tamper-evident seal is broken or missing. Keep out of reach of children</div>
</section>

<!-- Vitamin C line -->
<section class="label label--three vitc">
  <div class="label__band"></div>
  <div class="label__frame"></div>
  <div class="potency">High Potency Triglyceride Form</div>
  <svg class="seal" viewBox="0 0 56 48" aria-hidden="true"><circle cx="28" cy="24" r="22" fill="#b0561e"/><rect x="2" y="19" width="52" height="10" fill="#2fb341"/></svg>
  <div class="professional">PROFESSIONAL</div>
  <div class="directions">Directions: Take one or two softgels daily.</div>

  <div class="story">
    <p>Each fish gelatin capsule of Verda nox™ contains 1350 mg of Ultra-Intensity-Omega-3 (UIO-3) fish oil, which is our unique blend of EPA and DHA (55:25) in the triglyceride form. One capsule meets the recommendation of the National Cardio Council. Two capsules provide over 2700 mg of UIO-3 and 2500 mg of total omega-3: making Verda nox™ one of the highest professional grade fish oils available.</p>
    <p>Our specially formulated capsule was developed by Dr. Pellarino, an award-winning pioneer in the pharmaceutical industry. In research performed over decades, purified omega-3 is reported to promote healthy cholesterol and triglyceride levels, as well as supporting our heart, brain, and eyes.</p>
    <p>More recently, scientific research reports that the essential fatty acids as in Verda nox™ can help joint function and the health of the immune system. Especially because of our ultra-intensity triglyceride form, absorption of Verda nox™ is superior to other fish oil products with less fishy taste or burping.</p>
  </div>
  <div class="disclaimer">*These statements have not been evaluated by the Food and Drug Administration.<br>This product is not intended to diagnose, treat, cure or prevent disease.</div>

  <div class="brand">Verda<br>nox<sup>TM</sup></div>
  <div class="line-name">Vitamin C</div>
  <div class="grade">PHARMACEUTICAL GRADE</div>
  <ul class="features">
    <li>Triglyceride Form</li><li>Fish Gelatin</li><li>Clinically Proven Ratio</li><li>Superior Absorption</li><li>Ultra-Intensity Omega-3</li>
  </ul>
  <div class="pill pill--epa"><div class="pill__drop"><svg width="22" height="25" viewBox="0 0 22 25"><path d="M11 1 C15 8 20 12 20 16 A9 9 0 0 1 2 16 C2 12 7 8 11 1Z" fill="#f6c21c"/></svg><span>EPA</span></div>1500 <small>mg</small></div>
  <div class="pill pill--dha"><div class="pill__drop"><svg width="22" height="25" viewBox="0 0 22 25"><path d="M11 1 C15 8 20 12 20 16 A9 9 0 0 1 2 16 C2 12 7 8 11 1Z" fill="#f6c21c"/></svg><span>DHA</span></div>680 <small>mg</small></div>
  <div class="total">2500<small>mg</small><em>Total Omega-3</em></div>
  <div class="citrus" role="img" aria-label="Orange and lemon slices illustration"></div>
  <div class="citrus-note">Fresh Citrus Taste<br>Burp-Free</div>
  <div class="softgels">90 SOFTGELS DIETARY SUPPLEMENT</div>

  <div class="facts">
    <h2>Supplement Facts</h2>
    <div class="facts__serving"><span>Serving Size: 2 Softgels</span><span>Servings Per Container: 45</span></div>
    <div class="facts__row facts__row--head"><span>Amount Per Softgel Serving</span><span>% Daily Value*</span></div>
    <div class="facts__row"><span>Calories</span><span>30&nbsp;&nbsp;&nbsp;&nbsp;&nbsp;&nbsp;&nbsp;</span></div>
    <div class="facts__row"><span>Total Fat</span><span>3 g&nbsp;&nbsp;&nbsp;4%</span></div>
    <div class="facts__row"><span>Saturated Fat</span><span>0 g&nbsp;&nbsp;&nbsp;0%</span></div>
    <div class="facts__row"><span>Trans Fat</span><span>0 g&nbsp;&nbsp;1†&nbsp;</span></div>
    <div class="facts__row facts__row--split"><span><b>UIO-3</b> <small>(Fish Oil Concentrate)</small></span><span>2,750mg&nbsp;&nbsp;†&nbsp;&nbsp;</span></div>
    <div class="facts__row facts__row--sub"><span><b>EPA</b> <small>(Eicosapentaenoic Acid)</small></span><span>1,500mg&nbsp;&nbsp;†&nbsp;&nbsp;</span></div>
    <div class="facts__row facts__row--sub"><span><b>DHA</b> <small>(Docosahexaenoic Acid)</small></span><span>680mg&nbsp;&nbsp;†&nbsp;&nbsp;</span></div>
    <div class="facts__row facts__row--other"><span>Other Omega-3s</span><span>320mg&nbsp;&nbsp;†&nbsp;&nbsp;</span></div>
    <div class="facts__row facts__row--total"><span>Total Omega-3 Triglyceride</span><span>2,500mg&nbsp;&nbsp;†&nbsp;&nbsp;</span></div>
    <div class="facts__foot">* Daily Value based on a 2000 Calorie diet<br>† Daily Value not established</div>
  </div>
  <div class="ingredients">Other Ingredients: Gelatin capsule (fish gelatin, glycerin, purified water and natural flavor), d-limonene, Vitamin E and mixed tocopherols.</div>
  <div class="warning"><b>Warning:</b> Contains purified fish oil (from anchovies and sardines) gelatin (tilapia &amp; carp)</div>
  <div class="origin"><svg width="21" height="12" viewBox="0 0 21 12" aria-hidden="true"><rect width="21" height="12" fill="#c8102e"/><rect y="2" width="21" height="1.7" fill="#fff"/><rect y="5.4" width="21" height="1.7" fill="#fff"/><rect y="8.8" width="21" height="1.7" fill="#fff"/><rect width="9" height="6.5" fill="#3c3b6e"/></svg>Manufactured in USA with ingredients from around the world<br>42 Harbor Point Rd. Suite 12 , Palm Cove, FL 00000</div>
  <div class="contact">555.010.2427 | verdanox-example.com</div>
  <div class="storage">Store in a cool dry place. Do not take if tamper-evident seal is broken or missing. Keep out of reach of children</div>
</section>

</body>
</html>
```